V9 Web Design Project

New company website for Intel cyber security company.

Style should be cool, but remain appropriate for very serious subject matter and audience.

Target Market(s)

Target audience is government and the military

Navigation needs to include:
- About Us
- Services
- Careers
- Contact Us
- Contracts

As well as 2 feature areas - use "Technology Integration" and "Case Study" as the supporting headlines.

Industry/Entity Type

Security

Font styles to use
Sans Serif

Colors

Designer to choose colors to be used in the design.

Requirements
Must have
• Mountain imagery and theme.

Use logo attached.

New Tagline - "Securing the Continuum"
Nice to have
• Supporting imagery could include photos representative of security - avoid cliches.
Should not have
• Needs to be serious not frivolous

```html
<!DOCTYPE html>
<html lang="en">
<head>
<meta charset="utf-8">
<title>V9 Group — Securing the Continuum</title>
<link href="https://fonts.googleapis.com/css2?family=Open+Sans:wght@400;600;700&family=Raleway:wght@300;400;600;700&display=swap" rel="stylesheet">
<style>
:root{
  --nav-blue:#1f4e8c;
  --accent:#1f5fa8;
  --navy:#0b2650;
  --navy-deep:#061a3a;
  --ink:#333b45;
  --muted:#6d747c;
  --sand:#ecebe3;
  --line:#d9dadc;
  --white:#ffffff;
  --panel-dark:rgba(20,30,45,.78);
  --panel-light:rgba(255,255,255,.9);
}
*{box-sizing:border-box;margin:0;padding:0}
html,body{width:1200px;height:2632px;overflow:hidden}
body{font-family:"Open Sans",Arial,sans-serif;color:var(--ink);background:var(--white);position:relative}
h1,h2,h3,h4{font-family:"Raleway",Arial,sans-serif}

/* header */
.site-header{position:absolute;top:0;left:0;width:1200px;height:50px;display:flex;z-index:2}
.brand{width:250px;height:50px;background:var(--white);display:flex;align-items:center;padding-left:28px;font-family:"Raleway",sans-serif;font-weight:400;font-size:24px;letter-spacing:.5px;color:var(--ink)}
.main-nav{flex:1;background:var(--nav-blue);display:flex;justify-content:flex-end;align-items:center;padding-right:28px;gap:30px}
.main-nav a{color:var(--white);text-decoration:none;font-size:14px;font-weight:600;letter-spacing:.5px}

/* hero */
.hero{position:absolute;top:0;left:0;width:1200px;height:732px}
.hero-image{position:absolute;inset:0;background:linear-gradient(180deg,#4d6d93 0%,#8aa2bd 22%,#c7d2de 40%,#e9edf1 52%,#9aa6b4 68%,#3f4b5c 100%)}
.hero-title{position:absolute;top:276px;left:112px;color:var(--white);font-size:48px;font-weight:400;letter-spacing:3px}
.hero-rule{position:absolute;top:345px;left:112px;width:740px;height:1px;background:rgba(255,255,255,.6)}
.hero-cards{position:absolute;top:488px;left:112px;display:flex;gap:6px}
.hero-card{width:246px}
.hero-card h3{background:var(--panel-dark);color:var(--white);font-size:20px;font-weight:600;line-height:23px;padding:12px 16px;height:72px;text-transform:uppercase}
.hero-card-body{background:var(--panel-light);padding:12px 16px;height:124px;font-size:12px;line-height:17px;color:var(--muted)}
.hero-card-body .more{display:block;margin-top:8px;font-size:11px;font-weight:700;color:var(--ink)}
.hero-dots{position:absolute;top:684px;left:1022px;display:flex;gap:7px}
.hero-dots span{width:11px;height:11px;border:1.5px solid var(--white);border-radius:2px}
.hero-dots span.on{background:var(--white)}

/* intro */
.intro{position:absolute;top:756px;left:100px;width:1000px}
.intro h2{color:var(--accent);font-size:30px;font-weight:700;letter-spacing:.5px}
.intro p{margin-top:16px;font-size:19px;line-height:30px;color:var(--ink)}

/* technology */
.tech{position:absolute;top:912px;left:0;width:1200px;height:396px;background:linear-gradient(90deg,var(--navy-deep),var(--navy) 55%,#1b4b8a)}
.tech-globe{position:absolute;right:0;top:0;width:620px;height:396px;background:radial-gradient(circle at 62% 58%,#5aa8e6 0%,#2f6fb5 30%,#12396e 55%,rgba(11,38,80,0) 75%)}
.tech h2{position:absolute;top:60px;left:112px;color:var(--white);font-size:30px;font-weight:300;letter-spacing:1px}
.tech h2 strong{font-weight:700}
.tech p{position:absolute;top:128px;left:112px;width:520px;color:#dbe4f0;font-size:13px;line-height:22px}
.btn{display:inline-block;background:var(--navy-deep);color:var(--white);font-size:12px;font-weight:700;letter-spacing:1px;padding:12px 28px;border:1px solid rgba(255,255,255,.25)}
.tech .btn{position:absolute;top:310px;left:112px}

/* testimonials */
.clients{position:absolute;top:1308px;left:0;width:1200px;height:472px}
.section-title{text-align:center;font-size:30px;font-weight:300;letter-spacing:1px;color:var(--navy)}
.section-title strong{font-weight:700;color:var(--accent)}
.section-rule{width:1000px;height:1px;background:var(--line);margin:0 auto;position:relative}
.section-rule::after{content:"";position:absolute;left:560px;top:-1px;width:80px;height:3px;background:var(--accent)}
.clients .section-title{margin-top:66px}
.clients .section-rule{margin-top:16px}
.quotes{display:flex;justify-content:center;gap:60px;margin-top:34px}
.quote{width:260px;display:flex;gap:14px}
.quote-mark{font-family:"Raleway",sans-serif;font-size:60px;line-height:48px;color:#9aa1a8;font-weight:700}
.quote p{font-size:12.5px;line-height:19px;color:var(--muted)}
.quote-author{text-align:center;margin-top:12px;font-size:13px;font-weight:700;color:var(--ink)}
.avatar{width:80px;height:80px;border-radius:50%;margin:10px auto 0;background:radial-gradient(circle,#c9b8a6,#7a6a5c);border:3px solid var(--white);box-shadow:0 0 0 1px var(--line)}
.carousel-arrow{position:absolute;top:282px}
.carousel-arrow.left{left:110px}
.carousel-arrow.right{right:110px}

/* case study */
.case{position:absolute;top:1780px;left:0;width:1200px;height:500px;background:var(--sand)}
.case .section-title{margin-top:54px}
.case .section-rule{margin-top:16px;background:#cfcdc3}
.case-cards{display:flex;gap:12px;justify-content:center;margin-top:34px}
.case-card{width:268px;background:var(--white)}
.case-photo{height:140px;background:linear-gradient(135deg,#9aa8b8,#d7dde4 50%,#6f7f92)}
.case-card h4{padding:14px 14px 6px;font-size:15px;font-weight:700;line-height:20px;color:var(--ink);font-family:"Open Sans",sans-serif}
.case-card p{padding:0 14px 14px;font-size:11.5px;line-height:17px;color:var(--muted)}

/* footer */
.site-footer{position:absolute;top:2320px;left:0;width:1200px;height:312px;border-top:4px solid var(--accent)}
.footer-cols{display:flex;gap:120px;padding:34px 0 0 96px}
.footer-col h5{font-size:13px;font-weight:700;color:var(--ink);margin-bottom:10px}
.signup{display:flex;gap:14px;align-items:center}
.signup-field{width:270px;height:32px;border:1px solid var(--line);border-radius:16px;font-size:11px;color:#a0a5ab;padding:8px 14px}
.signup-btn{background:var(--accent);color:var(--white);border-radius:16px;font-size:13px;font-weight:600;padding:7px 22px}
.location{margin-top:26px;font-size:11.5px;line-height:17px;color:var(--muted)}
.contact-line{font-size:12px;color:var(--muted);line-height:20px}
.social{display:flex;gap:10px;margin-top:12px}
.social span{width:34px;height:34px;border-radius:50%;background:#8d949b}
.copyright{position:absolute;bottom:0;left:0;width:1200px;height:44px;background:#f3f3f3;font-size:11px;color:var(--muted);padding:15px 96px}
.copyright a{color:var(--accent);text-decoration:none}
</style>
</head>
<body>

<header class="site-header">
  <div class="brand">V9 Group</div>
  <nav class="main-nav">
    <a>HOME</a><a>ABOUT US</a><a>SERVICES</a><a>CAREERS</a><a>CONTACT US</a><a>CONTRACTS</a>
  </nav>
</header>

<section class="hero">
  <div class="hero-image" role="img" aria-label="Snow-capped mountain range under a blue sky"></div>
  <h1 class="hero-title">SECURING THE CONTINUUM</h1>
  <div class="hero-rule"></div>
  <div class="hero-cards">
    <article class="hero-card">
      <h3>What<br>we do</h3>
      <div class="hero-card-body">We deliver professional, technical and management services that protect critical missions across defense and civilian agencies.<span class="more">READ MORE</span></div>
    </article>
    <article class="hero-card">
      <h3>Our<br>philosophy</h3>
      <div class="hero-card-body">Integrity, precision and accountability guide every engagement, from first assessment through long-term support.<span class="more">READ MORE</span></div>
    </article>
    <article class="hero-card">
      <h3>Our<br>vision</h3>
      <div class="hero-card-body">To be the trusted partner that secures every stage of the mission continuum for our nation.<span class="more">READ MORE</span></div>
    </article>
  </div>
  <div class="hero-dots"><span class="on"></span><span></span><span></span><span></span></div>
</section>

<section class="intro">
  <h2>V9 GROUP HELPS CLIENTS ACHIEVE NEW HEIGHTS.</h2>
  <p>V9 Group, Inc. is an independent consulting firm providing professional, technical and management solutions to leading global corporations and the federal government.</p>
</section>

<section class="tech">
  <div class="tech-globe" role="img" aria-label="Glowing globe with network connections"></div>
  <h2><strong>TECHNOLOGY</strong> INTEGRATION SOLUTIONS</h2>
  <p>V9 Group provides scientific, engineering, administrative, technical operational and analytical support services to federal and military clients with emerging technologies relating to operational needs. V9 Group works closely with our clients to deliver innovative technology integration solutions. We support critical networks and systems that require secure, reliable solutions.</p>
  <span class="btn">READ MORE</span>
</section>

<section class="clients">
  <h2 class="section-title"><strong>WHAT</strong> OUR CLIENTS THINK</h2>
  <div class="section-rule"></div>
  <div class="quotes">
    <div>
      <div class="quote"><span class="quote-mark">&ldquo;</span><p>Their team understood our mission from day one and delivered a secure, dependable system ahead of schedule and within budget.</p></div>
      <div class="quote-author">Daniel Reyes</div>
      <div class="avatar" role="img" aria-label="Portrait of Daniel Reyes"></div>
    </div>
    <div>
      <div class="quote"><span class="quote-mark">&ldquo;</span><p>Clear reporting, disciplined engineers and real results. We rely on them for every phase of our network modernization work.</p></div>
      <div class="quote-author">Tom Harlow</div>
      <div class="avatar" role="img" aria-label="Portrait of Tom Harlow"></div>
    </div>
    <div>
      <div class="quote"><span class="quote-mark">&ldquo;</span><p>A partner that takes security as seriously as we do. Their analysts raised our readiness across several critical programs.</p></div>
      <div class="quote-author">Daniel Reyes</div>
      <div class="avatar" role="img" aria-label="Portrait of Daniel Reyes"></div>
    </div>
  </div>
  <svg class="carousel-arrow left" width="14" height="26" viewBox="0 0 14 26"><path d="M12 2 2 13l10 11" fill="none" stroke="#b5bac0" stroke-width="2"/></svg>
  <svg class="carousel-arrow right" width="14" height="26" viewBox="0 0 14 26"><path d="M2 2l10 11L2 24" fill="none" stroke="#b5bac0" stroke-width="2"/></svg>
</section>

<section class="case">
  <h2 class="section-title"><strong>CASE</strong> STUDY</h2>
  <div class="section-rule"></div>
  <div class="case-cards">
    <article class="case-card">
      <div class="case-photo" role="img" aria-label="Team meeting around a conference table"></div>
      <h4>Lorem ipsum dolor sit amet, adipiscing elit.</h4>
      <p>Assessment and integration work that hardened a regional command network against evolving threats.</p>
    </article>
    <article class="case-card">
      <div class="case-photo" role="img" aria-label="Analysts reviewing data on laptops"></div>
      <h4>Lorem ipsum dolor sit amet, adipiscing elit.</h4>
      <p>Secure cloud migration for a civilian agency, completed with zero downtime for field operations.</p>
    </article>
    <article class="case-card">
      <div class="case-photo" role="img" aria-label="Colleagues collaborating at a desk"></div>
      <h4>Lorem ipsum dolor sit amet, adipiscing elit.</h4>
      <p>Continuous monitoring program that cut incident response times across distributed defense sites.</p>
    </article>
    <article class="case-card">
      <div class="case-photo" role="img" aria-label="Professionals in a modern office"></div>
      <h4>Lorem ipsum dolor sit amet, adipiscing elit.</h4>
      <p>Training and advisory support that prepared program staff for new federal compliance standards.</p>
    </article>
  </div>
</section>

<footer class="site-footer">
  <div class="footer-cols">
    <div class="footer-col">
      <h5>NEWS LETTER</h5>
      <div class="signup"><span class="signup-field">Enter your email address here</span><span class="signup-btn">Sign up</span></div>
      <div class="location">
        <h5>Location</h5>
        Ridgeline Office<br>4410 Ridgeline Ave, Suite 210<br>Fairview, VA 20000
      </div>
    </div>
    <div class="footer-col">
      <h5>Connect with us</h5>
      <div class="contact-line">contact@v9group.example</div>
      <div class="contact-line">(555) 014-2070</div>
      <div class="social"><span></span><span></span><span></span></div>
    </div>
  </div>
  <div class="copyright">© 2014 V9 Group Inc. All Rights Reserved. | <a>Terms of Use</a> | <a>Privacy Policy</a></div>
</footer>

</body>
</html>
```